New company business cards with new company logo

We need a new business card designed as we have a new company logo and are going for a more 'flat design' look. Our company name is Veloristat and we are a global data focused Clinical Research Organisation. We'd ideally like one side with room for the individuals contact details, our full logo and our services - and one side which is quite plain, for example perhaps using the green triangular image attached with just the white 'V' in the center (also attached).

Industry/Entity Type

Business

Requirements
Must have
• Our main colour: #42b5a9
Please make text dark grey: #373737

```html
<!DOCTYPE html>
<html lang="en">
<head>
<meta charset="utf-8">
<title>Veloristat Business Cards</title>
<link href="https://fonts.googleapis.com/css2?family=Open+Sans:wght@400;600&display=swap" rel="stylesheet">
<style>
  :root {
    --brand-teal: #42b5a9;
    --brand-teal-soft: #d9f0ed;
    --text-grey: #373737;
    --divider-grey: #9a9a9a;
    --paper: #ffffff;
    --stage: #f4f7f7;
  }
  * { box-sizing: border-box; margin: 0; padding: 0; }
  html, body {
    width: 1200px; height: 1000px; overflow: hidden;
    background: var(--stage);
    font-family: "Open Sans", Arial, sans-serif;
    color: var(--text-grey);
  }
  .canvas { position: relative; width: 1200px; height: 1000px; }

  /* brand name at the top */
  .lockup {
    position: absolute; top: 50px; left: 0; width: 1200px;
    display: flex; justify-content: center; align-items: center; gap: 18px;
  }
  .lockup-dot { width: 90px; height: 90px; border-radius: 50%; background: var(--brand-teal); }
  .lockup-name { font-size: 44px; font-weight: 400; line-height: 1; }

  /* cards */
  .card {
    position: absolute; top: 380px; width: 490px; height: 290px;
    border-radius: 4px; overflow: hidden;
    box-shadow: 0 14px 34px rgba(40, 90, 85, 0.22);
  }
  .card-back { left: 80px; }
  .card-front { left: 630px; background: var(--paper); }

  .back-texture {
    position: absolute; inset: 0;
    background: linear-gradient(135deg, #6fb8ae 0%, #64b0a6 45%, #74bdb3 100%);
  }
  .back-mark {
    position: absolute; left: 50%; top: 50%; transform: translate(-50%, -50%);
    width: 130px; height: 130px; border-radius: 50%; background: var(--paper);
    display: flex; align-items: center; justify-content: center;
    font-size: 19px; font-weight: 600; color: var(--brand-teal);
  }

  .front-corner { position: absolute; top: 0; left: 0; }
  .front-circle { position: absolute; right: -70px; bottom: -120px; }
  .front-brand {
    position: absolute; left: 34px; top: 96px;
    display: flex; flex-direction: column; align-items: flex-start; gap: 12px;
  }
  .front-brand-dot { width: 64px; height: 64px; border-radius: 50%; background: var(--brand-teal); }
  .front-brand-name { font-size: 32px; font-weight: 400; line-height: 1; }
  .front-divider {
    position: absolute; left: 248px; top: 70px; width: 1px; height: 150px;
    background: var(--divider-grey);
  }
  .contact { position: absolute; left: 272px; top: 78px; }
  .contact-name { font-size: 24px; font-weight: 400; line-height: 1.1; }
  .contact-title { font-size: 15px; margin-bottom: 8px; }
  .contact-line { font-size: 13px; line-height: 1.55; }
</style>
</head>
<body>
<div class="canvas">

  <header class="lockup">
    <div class="lockup-dot"></div>
    <span class="lockup-name">Veloristat</span>
  </header>

  <section class="card card-back">
    <div class="back-texture" role="img" aria-label="Soft teal faceted triangle texture background"></div>
    <div class="back-mark">Veloristat</div>
  </section>

  <section class="card card-front">
    <svg class="front-corner" width="150" height="70" viewBox="0 0 150 70">
      <path d="M0 0 H150 A150 150 0 0 1 0 70 Z" fill="var(--brand-teal)"/>
    </svg>
    <svg class="front-circle" width="320" height="320" viewBox="0 0 320 320">
      <circle cx="160" cy="160" r="160" fill="var(--brand-teal-soft)"/>
    </svg>

    <div class="front-brand">
      <div class="front-brand-dot"></div>
      <span class="front-brand-name">Veloristat</span>
    </div>

    <div class="front-divider"></div>

    <div class="contact">
      <div class="contact-name">Name</div>
      <div class="contact-title">Title</div>
      <div class="contact-line">P: (XXX)-123-4567</div>
      <div class="contact-line">E: name@domain.com</div>
      <div class="contact-line">A: Location</div>
    </div>
  </section>

</div>
</body>
</html>
```